Car Branding for our VORNA Q Car Rental in Iceland

I am looking for eye popping and exciting design for the backend of our Vorna Q rental cars in Iceland.  We only rent out white Vorna Q, so base your designs only on a white Vorna Q.
Our Tagline is "Eco Powered Exploring" because Vorna is an electric car and all electricity in Iceland is made from renewable energy. The tagline must be visible on both sides of the car, and the back.
The website is www.glimmacarhire.com and must also be visible, at least in the back.

Target Market(s)
High End Tourist in Iceland
Industry/Entity Type
Tourism
Font styles to use
Serif
Sans Serif
Requirements
Must have
- Our logo and our tagline.

```html
<!DOCTYPE html>
<html lang="en">
<head>
<meta charset="utf-8">
<title>Glimma – Vorna Q Side Wrap</title>
<link href="https://fonts.googleapis.com/css2?family=Bebas+Neue&family=Roboto:wght@400&display=swap" rel="stylesheet">
<style>
  :root {
    --wrap-orange: #e8731f;
    --wrap-orange-deep: #d8651a;
    --wrap-white: #f4f5f6;
    --tagline-grey: #d9dce1;
    --page-bg: #ffffff;
    --panel-edge: #e3e4e6;
  }
  html, body {
    margin: 0;
    padding: 0;
    width: 1200px;
    height: 946px;
    overflow: hidden;
    background: var(--page-bg);
  }
  .canvas {
    position: relative;
    width: 1200px;
    height: 946px;
  }
  .side-panel {
    position: absolute;
    left: 60px;
    width: 1080px;
    height: 320px;
  }
  .side-panel--driver { top: 120px; }
  .side-panel--passenger { top: 520px; }
  .brand-name {
    font-family: "Bebas Neue", "Oswald", sans-serif;
    font-size: 64px;
    fill: var(--wrap-orange);
    letter-spacing: 1px;
  }
  .tagline {
    font-family: "Bebas Neue", "Oswald", sans-serif;
    font-size: 46px;
    fill: var(--tagline-grey);
    letter-spacing: 0.5px;
  }
  .web-address {
    font-family: "Roboto", Arial, sans-serif;
    font-size: 17px;
    fill: var(--tagline-grey);
    letter-spacing: 0.5px;
  }
</style>
</head>
<body>
<main class="canvas">

  <!-- Driver side: white front, orange rear -->
  <svg class="side-panel side-panel--driver" viewBox="0 0 1080 320" xmlns="http://www.w3.org/2000/svg">
    <rect class="panel-base" x="0" y="0" width="1080" height="320" rx="28" fill="var(--wrap-white)" stroke="var(--panel-edge)"/>
    <path class="panel-orange" d="M600 320 L760 0 L1052 0 Q1080 0 1080 28 L1080 292 Q1080 320 1052 320 Z" fill="var(--wrap-orange)"/>
    <line class="panel-stripe" x1="640" y1="320" x2="800" y2="0" stroke="var(--wrap-white)" stroke-width="10"/>
    <g class="brand-lockup">
      <rect x="300" y="110" width="44" height="44" fill="var(--wrap-orange)"/>
      <text class="brand-name" x="240" y="230">GLIMMA</text>
    </g>
    <g class="tagline-block" transform="rotate(-15 870 170)">
      <text class="tagline" x="760" y="150">ECO POWERED</text>
      <text class="tagline" x="760" y="196">EXPLORING</text>
      <line x1="760" y1="212" x2="930" y2="212" stroke="var(--tagline-grey)" stroke-width="2"/>
      <text class="web-address" x="762" y="240">glimmacarhire.com</text>
    </g>
  </svg>

  <!-- Passenger side: orange rear, white front -->
  <svg class="side-panel side-panel--passenger" viewBox="0 0 1080 320" xmlns="http://www.w3.org/2000/svg">
    <rect class="panel-base" x="0" y="0" width="1080" height="320" rx="28" fill="var(--wrap-white)" stroke="var(--panel-edge)"/>
    <path class="panel-orange" d="M480 320 L320 0 L28 0 Q0 0 0 28 L0 292 Q0 320 28 320 Z" fill="var(--wrap-orange)"/>
    <line class="panel-stripe" x1="440" y1="320" x2="280" y2="0" stroke="var(--wrap-white)" stroke-width="10"/>
    <g class="brand-lockup">
      <rect x="720" y="110" width="44" height="44" fill="var(--wrap-orange)"/>
      <text class="brand-name" x="660" y="230">GLIMMA</text>
    </g>
    <g class="tagline-block" transform="rotate(15 230 170)">
      <text class="tagline" x="110" y="130">ECO POWERED</text>
      <text class="tagline" x="130" y="176">EXPLORING</text>
      <line x1="130" y1="192" x2="300" y2="192" stroke="var(--tagline-grey)" stroke-width="2"/>
      <text class="web-address" x="120" y="220">glimmacarhire.com</text>
    </g>
  </svg>

</main>
</body>
</html>
```